Business Card and Stationery for Interior Design Company
Silver Kettle Design
Designers,
On the back of my card on want the following services listed:
Interior Decorating
Room Redesign
Space Planning
Paint Color Selection
Furnishings & Accessories
The fonts used in the logo are as follows:
fonts:
Kozuka Mincho Pr6N M
Miss Le Gatees (modified)
RT/KPF/JN Team
My tagline "Design with Vision" does NOT have to be the same font as the original logo font. Neither does my Name. In fact, tagline should probably be italic and my Name I'd like to see perhaps in a similar script font like the word INTERIOR.

```html
<!DOCTYPE html>
<html lang="en">
<head>
<meta charset="utf-8">
<title>Silver Kettle Design — Business Card</title>
<link href="https://fonts.googleapis.com/css2?family=Shippori+Mincho:wght@500&family=Cormorant+Garamond:ital,wght@0,400;0,500;1,400;1,500&family=Great+Vibes&display=swap" rel="stylesheet">
<style>
  :root {
    --page: #ececea;
    --card: #ffffff;
    --stripe: #f1f1f0;
    --panel: #d9d9d7;
    --brown: #5a4636;
    --ink: #3b3733;
    --teal: #5cc3c6;
    --teal-soft: #9fdcdc;
    --cream: #efe6c4;
    --rule: #c9c9c7;
  }
  * { margin: 0; padding: 0; box-sizing: border-box; }
  html, body { width: 1200px; height: 720px; overflow: hidden; }
  body {
    background: var(--page);
    display: flex;
    align-items: center;
    justify-content: center;
    gap: 40px;
  }
  .card {
    width: 540px;
    height: 309px;
    background: var(--card);
    box-shadow: 0 2px 6px rgba(0,0,0,0.12);
    position: relative;
    overflow: hidden;
  }
  /* Front */
  .card-front { display: flex; }
  .front-art {
    width: 300px;
    height: 100%;
    position: relative;
    background: repeating-linear-gradient(90deg, var(--card) 0 14px, var(--stripe) 14px 28px);
  }
  .room-illustration {
    position: absolute;
    left: 22px; top: 26px;
    width: 256px; height: 186px;
    border-radius: 6px;
    background: linear-gradient(160deg, var(--cream) 0%, #e6f3f1 45%, var(--teal-soft) 80%, var(--teal) 100%);
  }
  .tagline {
    position: absolute;
    left: 0; right: 0; bottom: 34px;
    text-align: center;
    font-family: "Cormorant Garamond", serif;
    font-style: italic;
    font-size: 15px;
    letter-spacing: 2.5px;
    color: var(--teal);
  }
  .front-info {
    flex: 1;
    background: var(--panel);
    text-align: center;
    padding-top: 40px;
  }
  .brand-name {
    font-family: "Shippori Mincho", serif;
    font-weight: 500;
    font-size: 22px;
    line-height: 1.2;
    color: var(--brown);
  }
  .person-name {
    margin-top: 40px;
    font-family: "Great Vibes", cursive;
    font-size: 26px;
    color: var(--teal);
  }
  .contact {
    margin-top: 42px;
    font-family: "Cormorant Garamond", serif;
    font-weight: 500;
    color: var(--ink);
    list-style: none;
  }
  .contact .phone { font-size: 15px; letter-spacing: 0.5px; margin-bottom: 3px; }
  .contact .line { font-size: 11.5px; line-height: 1.45; }
  /* Back */
  .services {
    position: absolute;
    left: 44px; top: 50%;
    transform: translateY(-50%);
    list-style: none;
    font-family: "Cormorant Garamond", serif;
    font-weight: 500;
    font-size: 14px;
    line-height: 1.85;
    color: var(--brown);
  }
  .services li::before {
    content: "";
    display: inline-block;
    width: 5px; height: 5px;
    margin: 0 10px 2px 0;
    background: var(--teal);
    border-radius: 50%;
  }
  .web-vertical {
    position: absolute;
    left: 264px; top: 155px;
    transform: translate(-50%, -50%) rotate(-90deg);
    font-family: "Cormorant Garamond", serif;
    font-size: 10px;
    letter-spacing: 1.5px;
    color: var(--teal);
    white-space: nowrap;
  }
  .divider {
    position: absolute;
    left: 280px; top: 64px;
    width: 1.5px; height: 180px;
    background: var(--teal);
  }
  .address-lines {
    position: absolute;
    left: 320px; top: 122px;
    width: 176px;
  }
  .address-lines span {
    display: block;
    height: 1px;
    background: var(--rule);
    margin-bottom: 26px;
  }
</style>
</head>
<body>
  <section class="card card-front">
    <div class="front-art">
      <div class="room-illustration" role="img" aria-label="Illustration of a furnished room: turquoise sofa with cushions, cream dresser, chandelier and framed art"></div>
      <p class="tagline">Design with Vision</p>
    </div>
    <div class="front-info">
      <h1 class="brand-name">Silver Kettle<br>Design</h1>
      <p class="person-name">Tessa Robanik</p>
      <ul class="contact">
        <li class="phone">555.014.2270</li>
        <li class="line">tessa@silverkettledesign.com</li>
        <li class="line">www.silverkettledesign.com</li>
      </ul>
    </div>
  </section>

  <section class="card card-back">
    <ul class="services">
      <li>Interior Decorating</li>
      <li>Room Redesign</li>
      <li>Space Planning</li>
      <li>Paint Color Selection</li>
      <li>Furnishings &amp; Accessories</li>
    </ul>
    <p class="web-vertical">www.silverkettledesign.com</p>
    <div class="divider"></div>
    <div class="address-lines">
      <span></span><span></span><span></span><span></span>
    </div>
  </section>
</body>
</html>
```